Asian simmer/ cooking sauce label

We are a established small gourmet condiment company with a range of products. This is a new product range of 6 simmer sauces that we would like a label designed that represents our brand but individualizes the new range.
the label should have a upmarket authentic feel and represent Asian cooking done in a home made kitchen
There will be six varieties it they will al have the same generic design only the product details will change

Our current range can be viewed on our website www.plumwicket.com.au

Butter Chicken has been uploaded. it is one of the products that will be used with the new label
I have uploaded a drinking chocolate label we use that has a black pattern

Target Market(s)

gourmet food shops, gifts stores

Colors

Designer to choose colors to be used in the design.

Requirements
Must have
• the labels needs to include product name. product description, ingredients, weight, nutritional panel, manufactures details and be a sized to suit jars which I will supply
• label size aprox 200mm long x 70mm high
Nice to have
• We prefer warm colours, gold, and black
• our brand name and logo
Should not have
• surprise me

```html
<!DOCTYPE html>
<html lang="en">
<head>
<meta charset="utf-8">
<title>Asian Simmer Cooking Sauce – Label</title>
<link rel="stylesheet" href="https://fonts.googleapis.com/css2?family=Jura:wght@500&family=Oswald:wght@300;400&family=Crimson+Text&family=Roboto:wght@400;700;900&display=swap">
<style>
  :root {
    --bg: #e2e2e2;
    --label-black: #151617;
    --orange: #e27a1e;
    --orange-dark: #a9481a;
    --orange-light: #f08a25;
    --white: #f4f4f4;
    --ribbon: #ececec;
    --ink: #1a1a1a;
    --gold: #c9b98f;
    --muted: #cfcfcf;
  }
  * { margin: 0; padding: 0; box-sizing: border-box; }
  html, body { width: 1200px; height: 797px; overflow: hidden; }
  body { background: var(--bg); position: relative; font-family: "Roboto", sans-serif; }

  .label {
    position: absolute; top: 228px; width: 340px; height: 344px;
    background: var(--label-black); overflow: hidden;
    box-shadow: 0 6px 18px rgba(0,0,0,.18);
  }
  .label--front { left: 184px; }
  .label--back { left: 684px; }

  .flavour-band {
    position: absolute; left: 0; right: 0; top: 106px; height: 186px;
    background: linear-gradient(90deg, var(--orange-dark) 0%, var(--orange) 45%, var(--orange-light) 100%);
  }

  /* front */
  .brand {
    position: absolute; left: 0; right: 0; top: 46px;
    display: flex; align-items: center; justify-content: center; gap: 8px;
  }
  .brand__mark { width: 14px; height: 14px; background: var(--gold); }
  .brand__name {
    font-family: "Roboto", sans-serif; font-weight: 700; font-size: 15px;
    letter-spacing: 3px; color: var(--gold);
  }
  .product-title {
    position: absolute; left: 44px; top: 128px;
    font-family: "Jura", sans-serif; font-weight: 500; font-size: 38px;
    letter-spacing: 0.5px; color: var(--white); white-space: nowrap;
    transform: scaleY(1.1); transform-origin: left top;
  }
  .ribbon { position: absolute; left: 13px; top: 176px; width: 180px; height: 50px; }
  .product-type {
    position: absolute; left: 45px; top: 182px;
    font-family: "Oswald", sans-serif; font-weight: 300; font-size: 31px;
    line-height: 1; color: var(--ink); letter-spacing: 0.5px;
  }
  .product-kind {
    position: absolute; left: 45px; top: 226px;
    font-family: "Oswald", sans-serif; font-weight: 300; font-size: 42px;
    line-height: 1; color: var(--white); letter-spacing: 0.5px;
  }
  .serving-photo {
    position: absolute; left: 161px; top: 180px; width: 140px; height: 112px;
    border-radius: 50%;
    background: radial-gradient(circle at 45% 45%, #b86a35 0%, #7a3b1c 55%, #4c6a2a 85%, #3f2a18 100%);
  }
  .net-weight {
    position: absolute; left: 47px; top: 306px;
    font-family: "Crimson Text", serif; font-size: 15px; color: var(--white);
  }
  .net-weight span { color: var(--orange); }

  /* back */
  .ingredients {
    position: absolute; left: 51px; top: 83px; width: 242px;
    font-size: 6.3px; line-height: 1.35; color: var(--muted);
  }
  .ingredients b { color: var(--white); }

  .nutrition {
    position: absolute; left: 51px; top: 140px; width: 232px; height: 82px;
    border: 1px solid var(--white); color: var(--white);
    display: grid; grid-template-columns: 62px 1fr 1fr; column-gap: 4px;
    padding: 2px 3px 10px 4px; font-size: 5.2px;
  }
  .nutrition__head { display: flex; flex-direction: column; gap: 3px; border-right: 1px solid var(--white); padding-right: 2px; }
  .nutrition__title { font-weight: 900; font-size: 9.5px; line-height: .95; }
  .nutrition__serving { font-weight: 700; font-size: 8.5px; line-height: 1.05; border-top: 1px solid var(--white); padding-top: 2px; }
  .nutrition__calories { display: flex; align-items: center; gap: 2px; border-top: 1px solid var(--white); padding-top: 2px; }
  .nutrition__calories small { font-weight: 700; font-size: 7.5px; line-height: .9; }
  .nutrition__calories strong { font-weight: 900; font-size: 13px; }
  .nutrition__col { display: flex; flex-direction: column; }
  .nutrition__row { display: flex; justify-content: space-between; border-bottom: 1px solid var(--white); padding: 1.2px 0; }
  .nutrition__row--caption { font-size: 3.8px; font-weight: 700; }
  .nutrition__row--sub { padding-left: 4px; }
  .nutrition__row b { font-weight: 700; }
  .nutrition__foot {
    position: absolute; left: 4px; bottom: 1px; font-size: 5px;
  }
  .nutrition__vitamins { position: absolute; left: 70px; bottom: 9px; font-size: 5px; }

  .allergens {
    position: absolute; left: 51px; top: 236px; width: 128px;
    font-size: 6.4px; line-height: 1.4; color: var(--white);
  }
  .allergens p + p { margin-top: 4px; }
  .care-icons { position: absolute; left: 188px; top: 236px; display: flex; gap: 8px; }
  .care-icons svg { width: 18px; height: 20px; }
</style>
</head>
<body>

<section class="label label--front">
  <div class="flavour-band"></div>
  <div class="brand">
    <span class="brand__mark"></span>
    <span class="brand__name">HARLOW PANTRY</span>
  </div>
  <h1 class="product-title">ASIAN SIMMER</h1>
  <svg class="ribbon" viewBox="0 0 180 50" aria-hidden="true">
    <path d="M0 8 L180 8 L170 50 L8 46 L18 30 Z" fill="var(--ribbon)"/>
    <path d="M0 8 Q90 -6 180 14" fill="none" stroke="var(--ribbon)" stroke-width="8"/>
  </svg>
  <p class="product-type">COOKING</p>
  <p class="product-kind">SAUCE</p>
  <div class="serving-photo" role="img" aria-label="Plate of roasted chicken wings with fries, dipping sauce and fresh parsley"></div>
  <p class="net-weight"><span>NET</span> 420g</p>
</section>

<section class="label label--back">
  <div class="flavour-band"></div>
  <p class="ingredients"><b>INGREDIENTS:</b> Bananas, apples, palm unsweetened chocolate, cocoa powder, kernel oil, sugar, chicory root fiber, soy lecithin, natural flavor, sea salt, cocoa butter.</p>

  <div class="nutrition">
    <div class="nutrition__head">
      <div class="nutrition__title">Nutrition<br>Facts</div>
      <div class="nutrition__serving">Serving size<br>1 bar (38g)</div>
      <div class="nutrition__calories"><small>Calories<br>per serving</small><strong>130</strong></div>
    </div>
    <div class="nutrition__col">
      <div class="nutrition__row nutrition__row--caption"><span>Amount/Serving</span><span>% Daily Value</span></div>
      <div class="nutrition__row"><span><b>Total Fat</b> 2g</span><b>3%</b></div>
      <div class="nutrition__row nutrition__row--sub"><span>Sat. Fat 1.5g</span><b>8%</b></div>
      <div class="nutrition__row nutrition__row--sub"><span><i>Trans</i> Fat 0g</span></div>
      <div class="nutrition__row nutrition__row--sub"><span>Polyunsaturated Fat 0g</span></div>
      <div class="nutrition__row nutrition__row--sub"><span>Monounsaturated Fat 0g</span></div>
      <div class="nutrition__row"><span><b>Cholesterol</b> 0mg</span><b>0%</b></div>
    </div>
    <div class="nutrition__col">
      <div class="nutrition__row nutrition__row--caption"><span>Amount/Serving</span><span>% Daily Value</span></div>
      <div class="nutrition__row"><span><b>Sodium</b> 15mg</span><b>1%</b></div>
      <div class="nutrition__row"><span><b>Total Carb.</b> 29g</span><b>11%</b></div>
      <div class="nutrition__row nutrition__row--sub"><span>Fiber 4g</span><b>14%</b></div>
      <div class="nutrition__row nutrition__row--sub"><span>Total Sugars 18g</span></div>
      <div class="nutrition__row nutrition__row--sub"><span>Incl. 1g of Added Sugars</span><b>2%</b></div>
      <div class="nutrition__row"><span><b>Protein</b> 1g</span></div>
    </div>
    <p class="nutrition__vitamins">Vitamin D 0% • Calcium 0% • Iron 6% • Potassium 4%</p>
    <p class="nutrition__foot">Brought to you by <b>Fernleaf Foods</b> • P.O. Box 218, Ashgrove, QLD 4060</p>
  </div>

  <div class="allergens">
    <p><b>Allergen Information:</b> Contains soy.</p>
    <p>Made in a facility that processes peanuts, tree nuts, sesame seeds and dairy.</p>
  </div>

  <div class="care-icons">
    <svg viewBox="0 0 18 20" aria-label="Flammable"><path d="M9 2 C12 7 14 9 13 13 C12 16 6 16 5 13 C4 10 7 9 7 6 C9 8 9 10 10 11 C11 9 10 5 9 2 Z" fill="none" stroke="var(--white)" stroke-width="1.4"/><line x1="2" y1="18" x2="16" y2="18" stroke="var(--white)" stroke-width="1.4"/></svg>
    <svg viewBox="0 0 18 20" aria-label="Recyclable"><path d="M9 3 L13 9 M13 9 L10 9 M13 9 L14 6 M15 12 L11 17 M11 17 L12 14 M11 17 L14 17 M5 16 L2 10 M2 10 L2 13 M2 10 L5 11" fill="none" stroke="var(--white)" stroke-width="1.6" stroke-linecap="round"/></svg>
    <svg viewBox="0 0 18 20" aria-label="Dispose in bin"><rect x="3" y="8" width="7" height="10" fill="none" stroke="var(--white)" stroke-width="1.3"/><line x1="2" y1="7" x2="11" y2="7" stroke="var(--white)" stroke-width="1.3"/><circle cx="14" cy="3" r="1.5" fill="var(--white)"/><path d="M14 5 L14 12 L12 18 M14 12 L16 18 M14 7 L11 9" fill="none" stroke="var(--white)" stroke-width="1.3"/></svg>
  </div>
</section>

</body>
</html>
```